"Tales of Quiet Harbors" Book Cover Design

I am seeking a dynamic, modern, and professional cover design for a book focused on groundbreaking science that explores how a supplement called plasmalogens can revitalize the brain, prevent Alzheimer’s, and safeguard memories. The design should strike a balance between being visually appealing and conveying the seriousness of the topic.

Target Market(s)

The target audience includes individuals who are curious about cutting-edge science and proactive approaches to brain health, as well as those seeking to better understand how to protect their cognitive functions and memories. The cover should resonate with readers interested in health, science, and self-improvement, while reflecting the book’s informative and empowering tone.

Requirements
Must have
• The quotation across the top of the page (this is a placeholder for now, it will be changed eventually) and the author's name.
Should not have
• You don't need to use the puzzle idea!

```html
<!DOCTYPE html>
<html lang="en">
<head>
<meta charset="utf-8">
<title>Tales of Quiet Harbors — Book Cover</title>
<link rel="stylesheet" href="https://fonts.googleapis.com/css2?family=Barlow+Condensed:wght@400;500;700;800&family=Nunito:wght@700;800&display=swap">
<style>
  :root {
    --backdrop: #4a4a4a;
    --paper: #ffffff;
    --accent: #c97d3c;
    --ink: #272727;
    --art-light: #e7b48e;
    --art-deep: #b5703f;
  }
  * { margin: 0; padding: 0; box-sizing: border-box; }
  html, body {
    width: 1200px;
    height: 1200px;
    overflow: hidden;
    background: var(--backdrop);
  }
  .cover {
    position: absolute;
    left: 233px;
    top: 50px;
    width: 733px;
    height: 1100px;
    background: var(--paper);
    overflow: hidden;
  }
  .endorsement {
    position: absolute;
    left: 0;
    right: 0;
    top: 52px;
    text-align: center;
    font-family: "Nunito", sans-serif;
  }
  .endorsement-quote {
    font-weight: 800;
    font-size: 20px;
    color: var(--accent);
    letter-spacing: 0.1px;
  }
  .endorsement-source {
    margin-top: 8px;
    font-weight: 800;
    font-size: 18px;
    color: var(--ink);
  }
  .title {
    position: absolute;
    left: 0;
    top: 0;
    width: 733px;
    height: 600px;
  }
  .title text {
    font-family: "Barlow Condensed", sans-serif;
  }
  .title-lead { fill: var(--accent); font-weight: 700; }
  .title-small { fill: var(--ink); font-weight: 500; }
  .title-main { fill: var(--ink); font-weight: 800; }
  .subtitle {
    position: absolute;
    left: 0;
    right: 0;
    top: 606px;
    text-align: center;
    font-family: "Nunito", sans-serif;
    font-weight: 800;
    font-size: 20.5px;
    line-height: 30px;
    color: var(--ink);
  }
  .subtitle-highlight { color: var(--accent); }
  .cover-art {
    position: absolute;
    left: 0;
    top: 684px;
    width: 733px;
    height: 390px;
    background:
      radial-gradient(ellipse 48% 46% at 63% 52%, var(--art-light) 0%, var(--art-deep) 70%, rgba(181,112,63,0) 100%);
  }
  .author {
    position: absolute;
    left: 55px;
    top: 1022px;
    font-family: "Nunito", sans-serif;
    font-weight: 800;
    font-size: 21px;
    color: var(--accent);
    letter-spacing: 0.3px;
  }
</style>
</head>
<body>
  <main class="cover">
    <header class="endorsement">
      <p class="endorsement-quote">“An Incredible guide to protecting your mind and memories.”</p>
      <p class="endorsement-source">Dr. Anil Mehra, MD</p>
    </header>

    <svg class="title" viewBox="0 0 733 600" aria-label="Tales of Quiet Harbors">
      <text class="title-lead" x="55" y="349" font-size="300" textLength="305" lengthAdjust="spacingAndGlyphs">TALES</text>
      <text class="title-small" x="372" y="256" font-size="167">OF</text>
      <text class="title-small" x="372" y="349" font-size="115" textLength="308" lengthAdjust="spacingAndGlyphs">QUIET</text>
      <text class="title-main" x="55" y="582" font-size="290" textLength="625" lengthAdjust="spacingAndGlyphs">HARBORS</text>
    </svg>

    <p class="subtitle">
      <span class="subtitle-highlight">RESTORE YOUR MEMORY</span>, PREVENT ALZHEIMER’S<br>
      AND REVERSE THE AGE OF YOUR MIND
    </p>

    <div class="cover-art" role="img" aria-label="Illustration of a human brain with a hand placing a missing piece"></div>

    <p class="author">THOMAS ELRIDGE, MD</p>
  </main>
</body>
</html>
```